Spices producer needs product label design.

I need a two label design of 90mm(H) x 60mm(H) for multiple line of spices and other product. First label for the front should have the logo, and second label should be the same as the first but without the logo. I would like the same dark reddish colour on my logo for the design if possible or similar. This label will be use for multiple products, so a clear in-between space is important to add information and change product name for printing . I would prefer a mixture of traditional and rustic style.
I have attached my logos and sample on how I would like the look.

Target Market(s)

25-60 women and men.

Industry/Entity Type

Retail

Requirements
Must have
• As stated above.
Nice to have
• Please see attached sample .
Should not have
• Multiple colours, animation design.

```html
<!DOCTYPE html>
<html lang="en">
<head>
<meta charset="utf-8">
<title>Talvo Spices – Product Label</title>
<link rel="stylesheet" href="https://fonts.googleapis.com/css2?family=Lora:wght@700&display=swap">
<style>
  :root {
    --paper: #ffffff;
    --label-red: #a61d25;
    --ring-red: #b8302c;
    --band-gold: #f2a31e;
    --seal-gold: #f8a91c;
    --ink-maroon: #7a1216;
  }
  * { margin: 0; padding: 0; box-sizing: border-box; }
  html, body {
    width: 1200px;
    height: 799px;
    overflow: hidden;
    background: var(--paper);
  }
  .canvas {
    position: relative;
    width: 1200px;
    height: 799px;
    background: var(--paper);
  }
  .label {
    position: absolute;
    left: 35px;
    top: 23px;
    width: 1128px;
    height: 753px;
    background: var(--label-red);
  }
  .trim-band {
    position: absolute;
    left: 0;
    width: 100%;
    height: 46px;
    background: linear-gradient(180deg, var(--band-gold) 0%, #e99018 50%, var(--band-gold) 100%);
  }
  .trim-band--top { top: 51px; }
  .trim-band--bottom { top: 645px; }
  .seal {
    position: absolute;
    left: 322px;
    top: 120px;
    width: 478px;
    height: 478px;
  }
  .seal svg { display: block; width: 100%; height: 100%; }
  .brand {
    position: absolute;
    left: 322px;
    top: 120px;
    width: 478px;
    height: 478px;
    display: flex;
    flex-direction: column;
    align-items: center;
    justify-content: center;
    font-family: "Lora", Georgia, serif;
    font-weight: 700;
    color: var(--ink-maroon);
    text-align: center;
    line-height: 1;
  }
  .brand__name {
    font-size: 78px;
    letter-spacing: 2px;
  }
  .brand__line {
    font-size: 70px;
    margin-top: 34px;
  }
</style>
</head>
<body>
  <main class="canvas">
    <section class="label">
      <div class="trim-band trim-band--top" role="img" aria-label="Gold decorative diamond-pattern border band"></div>

      <div class="seal">
        <svg viewBox="0 0 478 478" aria-hidden="true">
          <circle class="seal__ring" cx="239" cy="239" r="237" fill="var(--ring-red)" role="img" aria-label="Scalloped lace ornament ring"></circle>
          <circle class="seal__disc" cx="239" cy="239" r="207" fill="var(--seal-gold)"></circle>
        </svg>
      </div>

      <div class="brand">
        <span class="brand__name">TALVO</span>
        <span class="brand__line">spices</span>
      </div>

      <div class="trim-band trim-band--bottom" role="img" aria-label="Gold decorative diamond-pattern border band"></div>
    </section>
  </main>
</body>
</html>
```